Redesign our iOS App Design mockups

- Redesign our current Velorin App Mockup
- Keep the design simple so that programmers do not have to do too much extra work to make your design work.
- Look at the attached website screenshot for the overall look and feel, and color scheme
- Convert the attached vector logo to iOS Icon format.
- Deliver all graphics in the density required for Velorin QT Prime.
- I have attached the current iOS mockup in a .ZIP file but you can view it here as well: https://boards.mockwharf.com/view/QRTLPW8KXB2

Target Market(s)

Mostly Male Internet Consumers between the ages of 20 and 35

Industry/Entity Type

Internet

Colors

Designer to choose colors to be used in the design.

Requirements
Must have
• - Deliver all graphics in the density required for Velorin QT Prime
• - Should also look good on Tablix and Tablix plus
• - Design type should be “FLAT.”
• - Spell out fonts used in the design and where they are used. Also, include font sizes.
• - Please use ALL the elements in each page and use all placements and text EXACTLY. Please do not improvise with text or components.
• I have designed the mockup exactly the way I like it. I just want it to made to look better.
Should not have

```html
<!DOCTYPE html>
<html lang="en">
<head>
<meta charset="utf-8">
<title>Nestlock iOS App Screens</title>
<link href="https://fonts.googleapis.com/css2?family=Montserrat:wght@400;500;600;700&display=swap" rel="stylesheet">
<style>
:root{
  --coral:#f4675c;
  --ink:#1d1d22;
  --muted:#9a9aa2;
  --line:#e6e6ea;
  --veil:#4a4457;
  --white:#ffffff;
  --canvas:#ffffff;
}
*{box-sizing:border-box;margin:0;padding:0}
html,body{width:1200px;height:1114px;overflow:hidden;background:var(--canvas)}
body{font-family:"Montserrat",sans-serif;color:var(--ink)}
.board{position:absolute;left:0;top:0;width:1500px;height:1392px;transform:scale(.8);transform-origin:0 0}
.screen{position:absolute;width:288px;height:624px;border-radius:36px;overflow:hidden;background:var(--white);box-shadow:0 0 0 1px #ececef}
.screen *{position:absolute}
.splash{background:var(--coral);color:var(--white)}
.brand-dot{border-radius:50%}
.brand-name{font-weight:700;letter-spacing:.5px;white-space:nowrap}
.center{left:0;width:100%;text-align:center}
.label{font-size:8px;color:var(--muted);font-weight:500}
.field-value{font-size:14px;color:var(--coral);font-weight:600}
.underline{height:1px;background:var(--line)}
.btn{background:var(--coral);color:var(--white);border-radius:4px;font-size:8px;font-weight:700;display:flex;align-items:center;justify-content:center;letter-spacing:.3px}
.btn-outline{background:var(--white);color:var(--coral);border:1px solid var(--coral)}
.clear{width:12px;height:12px;border-radius:50%;background:var(--coral)}
.section{font-size:8px;color:var(--muted);font-weight:600;letter-spacing:.6px}
.row-text{font-size:8.5px;font-weight:600;color:var(--ink)}
.flag{width:17px;height:17px;border-radius:50%}
.star{width:13px;height:13px;border-radius:50%;background:#c9c9cf}
.star.on{background:var(--coral)}
.title{font-size:12px;font-weight:600}
.ping{width:40px;text-align:center;font-size:6.5px;font-weight:600}
.ping span{position:static;display:block;margin:0 auto 2px;width:11px;height:11px;border-radius:50%;border:2px solid var(--coral)}
.settings-head{font-size:11px;color:var(--muted);font-weight:600;letter-spacing:.5px}
.item-title{font-size:8.5px;font-weight:700}
.item-desc{font-size:8px;color:var(--muted);line-height:11px}
.menu-item{font-size:11.5px;font-weight:600;left:37px}
.menu-icon{left:15px;width:9px;height:9px;border-radius:2px;background:#f7b3ad}
.footer-link{font-size:8px;font-weight:600}
</style>
</head>
<body>
<main class="board">

  <!-- Splash -->
  <section class="screen splash" style="left:61px;top:36px">
    <div class="brand-dot" style="left:119px;top:183px;width:50px;height:50px;background:var(--white)"></div>
    <div class="brand-name center" style="top:290px;font-size:23px">NESTLOCK</div>
    <div class="center" style="top:332px;font-size:8px;font-weight:600">Loading</div>
    <div style="left:68px;top:376px;width:150px;height:2px;background:rgba(255,255,255,.3)"></div>
    <div style="left:68px;top:376px;width:77px;height:2px;background:var(--white)"></div>
    <div class="center" style="top:603px;font-size:6.5px;opacity:.8">Version v1.0a</div>
  </section>

  <!-- Login -->
  <section class="screen" style="left:427px;top:36px">
    <div class="brand-dot" style="left:115px;top:80px;width:58px;height:58px;background:var(--coral)"></div>
    <div class="brand-name center" style="top:162px;font-size:18px;color:var(--ink)">NESTLOCK</div>
    <div class="label" style="left:40px;top:272px">User ID:</div>
    <div class="field-value" style="left:45px;top:297px">email@example.com</div>
    <div class="clear" style="left:235px;top:300px"></div>
    <div class="underline" style="left:36px;top:320px;width:216px"></div>
    <div class="label" style="left:40px;top:373px">Password</div>
    <svg style="left:234px;top:371px" width="14" height="10" viewBox="0 0 14 10"><path d="M1 5c2-3.5 10-3.5 12 0-2 3.5-10 3.5-12 0z" fill="none" stroke="#1d1d22" stroke-width="1.3"/><circle cx="7" cy="5" r="1.6" fill="#1d1d22"/><path d="M3 9l8-8" stroke="#1d1d22" stroke-width="1.3"/></svg>
    <div class="underline" style="left:36px;top:390px;width:216px;background:#cfcfd4"></div>
    <div style="right:36px;top:402px;font-size:8px;font-weight:600;color:var(--coral)">Forgot Password ?</div>
    <div class="btn" style="left:66px;top:464px;width:156px;height:32px">LOGIN</div>
    <div class="center" style="top:578px;font-size:8px;font-weight:500">Don't have an account yet? <b style="position:static;color:var(--coral)">Sign up here.</b></div>
  </section>

  <!-- Reset password -->
  <section class="screen" style="left:793px;top:36px">
    <svg style="left:27px;top:60px" width="12" height="20" viewBox="0 0 12 20"><path d="M10 2L2 10l8 8" fill="none" stroke="var(--coral)" stroke-width="2.2" stroke-linecap="round"/></svg>
    <div class="title center" style="top:63px">Reset Password</div>
    <div style="left:27px;top:125px;font-size:14px;font-weight:600">Did you forget your password?</div>
    <p style="left:27px;top:156px;width:242px;font-size:7px;line-height:10px;color:var(--muted)">If you have forgotten your password, enter the email address assosciate with your account into the box blow and we will send you instructions on how to reset your passsword to your email account.</p>
    <div class="label" style="left:40px;top:273px">Email Address:</div>
    <div class="field-value" style="left:45px;top:298px">email@example.com</div>
    <div class="clear" style="left:235px;top:300px"></div>
    <div class="underline" style="left:36px;top:322px;width:216px"></div>
    <div class="btn" style="left:70px;top:362px;width:148px;height:32px">Reset Password</div>
    <div class="btn btn-outline" style="left:70px;top:444px;width:148px;height:32px">
      <svg style="position:static;margin-right:14px" width="12" height="10" viewBox="0 0 12 10"><path d="M11 5H2M5 1L1 5l4 4" fill="none" stroke="var(--coral)" stroke-width="1.4"/></svg>Back to Login
    </div>
  </section>

  <!-- Home -->
  <section class="screen" style="left:1159px;top:36px">
    <div style="left:28px;top:62px;width:24px;height:2px;background:var(--ink)"></div>
    <div style="left:28px;top:69px;width:16px;height:2px;background:var(--ink)"></div>
    <div class="brand-name center" style="top:58px;font-size:17px">NESTLOCK</div>
    <div class="ping" style="left:236px;top:55px"><span></span>Ping Test</div>
    <div class="center" style="top:120px;font-size:7.5px;color:var(--muted);font-weight:500">Not Connected</div>
    <div class="btn" style="left:67px;top:143px;width:155px;height:32px">Quck Connect</div>

    <div class="section" style="left:28px;top:228px">FAVORITES</div>
    <div class="underline" style="left:28px;top:241px;width:244px"></div>
    <div class="flag" style="left:27px;top:261px;background:linear-gradient(#1d1d22 33%,#e3342f 33% 66%,#f6c445 66%)"></div>
    <div class="row-text" style="left:58px;top:265px">Germany</div>
    <div class="star on" style="left:253px;top:263px"></div>

    <div class="section" style="left:28px;top:303px">SPECIALITY SERVERS</div>
    <div class="underline" style="left:28px;top:316px;width:244px"></div>
    <div style="left:33px;top:334px;width:9px;height:9px;border-top:2px solid var(--ink);border-bottom:2px solid var(--ink)"></div>
    <div class="row-text" style="left:58px;top:334px">Streaming Servers</div>
    <div style="left:33px;top:359px;width:9px;height:9px;border:1.3px solid var(--ink)"></div>
    <div class="row-text" style="left:58px;top:359px">P2P Severs</div>
    <div style="left:33px;top:384px;width:9px;height:9px;border-radius:50%;border:1.3px solid var(--ink)"></div>
    <div class="row-text" style="left:58px;top:384px">Onion over VPN</div>

    <div class="section" style="left:28px;top:416px">COUNTRY</div>
    <div class="underline" style="left:28px;top:428px;width:244px"></div>
    <div class="flag" style="left:27px;top:445px;background:linear-gradient(135deg,#2f3d8f 40%,#e3342f 40% 60%,#f2f2f2 60%)"></div>
    <div class="row-text" style="left:58px;top:449px">USA</div><div class="star" style="left:253px;top:447px"></div>
    <div class="flag" style="left:27px;top:477px;background:linear-gradient(#2f3d8f 40%,#e3342f 40% 60%,#2f3d8f 60%)"></div>
    <div class="row-text" style="left:58px;top:481px">UK</div><div class="star" style="left:253px;top:479px"></div>
    <div class="flag" style="left:27px;top:509px;background:radial-gradient(circle,#e3342f 35%,#ffffff 36%)"></div>
    <div class="row-text" style="left:58px;top:513px">Canda</div><div class="star" style="left:253px;top:511px"></div>
    <div class="flag" style="left:27px;top:541px;background:linear-gradient(#f39a3a 33%,#ffffff 33% 66%,#3c9a4a 66%)"></div>
    <div class="row-text" style="left:58px;top:545px">India</div><div class="star" style="left:253px;top:543px"></div>
    <div class="flag" style="left:27px;top:573px;background:linear-gradient(#e3342f 33%,#ffffff 33% 66%,#2f3d8f 66%)"></div>
    <div class="row-text" style="left:58px;top:577px">France</div><div class="star" style="left:253px;top:575px"></div>
    <div class="flag" style="left:27px;top:605px;background:linear-gradient(#e3342f 50%,#ffffff 50%)"></div>
    <div class="row-text" style="left:56px;top:609px">Singapore</div><div class="star" style="left:253px;top:607px"></div>
  </section>

  <!-- Drawer -->
  <section class="screen" style="left:61px;top:724px">
    <div style="left:192px;top:0;width:96px;height:624px;background:var(--veil)"></div>
    <div class="brand-dot" style="left:20px;top:72px;width:32px;height:32px;background:var(--coral)"></div>
    <div class="brand-name" style="left:64px;top:82px;font-size:14px">NESTLOCK</div>
    <div style="left:95px;top:100px;font-size:6.5px;color:var(--muted);font-weight:600">Version v1.0a</div>
    <div style="left:0;top:157px;width:192px;height:28px;background:var(--coral)"></div>
    <div class="menu-icon" style="top:167px;background:#fbc6c1"></div>
    <div class="menu-item" style="top:163px;color:var(--white);font-weight:700">Home</div>
    <div class="menu-icon" style="top:212px"></div>
    <div class="menu-item" style="top:208px">Settings</div>
    <div class="menu-icon" style="top:256px"></div>
    <div class="menu-item" style="top:252px">Support Center</div>
    <div class="menu-icon" style="top:301px"></div>
    <div class="menu-item" style="top:297px">Logout</div>
  </section>

  <!-- Settings -->
  <section class="screen" style="left:424px;top:724px">
    <svg style="left:27px;top:60px" width="12" height="20" viewBox="0 0 12 20"><path d="M10 2L2 10l8 8" fill="none" stroke="var(--coral)" stroke-width="2.2" stroke-linecap="round"/></svg>
    <div class="title center" style="top:63px">Settings</div>
    <div class="ping" style="left:232px;top:58px"><span></span>Ping Test</div>
    <div class="settings-head" style="left:26px;top:134px">APP SETTINGS</div>
    <div class="underline" style="left:26px;top:152px;width:244px"></div>
    <div class="item-title" style="left:26px;top:168px">Kill Switch</div>
    <div class="item-desc" style="left:26px;top:183px;width:170px">Cuts Internet connectivity when your VPN connection gets lost</div>
    <svg style="left:241px;top:177px" width="19" height="19" viewBox="0 0 19 19"><circle cx="9.5" cy="9.5" r="9.5" fill="var(--coral)"/><path d="M5.5 9.8l2.7 2.7 5.3-5.5" fill="none" stroke="#fff" stroke-width="1.8"/></svg>
    <div class="underline" style="left:26px;top:220px;width:244px"></div>
    <svg style="left:26px;top:244px" width="16" height="15" viewBox="0 0 16 15"><path d="M2 6a6 6 0 0 1 11-2M14 9a6 6 0 0 1-11 2" fill="none" stroke="#1d1d22" stroke-width="1.6"/><path d="M13 1v3h-3M3 14v-3h3" fill="none" stroke="#1d1d22" stroke-width="1.6"/></svg>
    <div class="item-title" style="left:57px;top:247px">Protocols</div>
    <div class="underline" style="left:26px;top:282px;width:244px"></div>
    <svg style="left:26px;top:290px" width="16" height="15" viewBox="0 0 16 15"><path d="M9 2H2v11h7M6 7.5h9M12 4.5l3 3-3 3" fill="none" stroke="#1d1d22" stroke-width="1.6"/></svg>
    <div class="item-title" style="left:57px;top:294px">Logout</div>
    <div class="footer-link" style="left:26px;top:604px">Terms of Service</div>
    <div class="footer-link" style="left:122px;top:603px">Privacy Policy</div>
    <div style="right:18px;top:604px;font-size:8px;color:var(--muted)">1.0a version</div>
  </section>

  <!-- Protocol selection -->
  <section class="screen" style="left:787px;top:724px">
    <svg style="left:27px;top:61px" width="12" height="20" viewBox="0 0 12 20"><path d="M10 2L2 10l8 8" fill="none" stroke="var(--coral)" stroke-width="2.2" stroke-linecap="round"/></svg>
    <div class="title center" style="top:64px">Settings</div>
    <div class="ping" style="left:232px;top:59px"><span></span>Ping Test</div>
    <div class="settings-head" style="left:26px;top:136px">PROTOCOL SELECTION</div>
    <div class="underline" style="left:26px;top:154px;width:244px"></div>
    <div class="item-title" style="left:26px;top:176px">Automatic</div>
    <div class="item-desc" style="left:26px;top:191px">Let Nestlock chose the best protocol</div>
    <div class="underline" style="left:26px;top:220px;width:244px"></div>
    <div class="item-title" style="left:26px;top:240px">IPSec</div>
    <div class="item-desc" style="left:26px;top:255px">The most secure protocol</div>
    <div class="underline" style="left:26px;top:286px;width:244px"></div>
    <div class="item-title" style="left:26px;top:303px">IKEv2</div>
    <div class="item-desc" style="left:26px;top:320px">The most stable protocol</div>
  </section>

</main>
</body>
</html>
```